Safety Brochure for Industry Assocations

This is an 8.5 x 11 single sided brochure for our Occupational Health and Safety Data Analytics software. If you need to use stock images we will pay for them.

Please incorporate our logo and some of the images. No need to incorporate them all. We like the idea of the boots being at the bottom of the page but we're open to other ideas.

Please note that we intend to mail this brochure to different industries so it should be generic (i.e. not construction specific).

Target Market(s)

Safety and Industry Organisations for construction, mining, forestry and oil and gas industries.

Industry/Entity Type

Industry

Font styles to use
Sans Serif

Colors

Designer to choose colors to be used in the design.

Requirements
Must have
• We are a software company that produces safety software. Our customers are companies that engage in dangerous work and use our software to improve their worker's safety. The look and feel should convey the fact that:
• -We are Big Data
• -We are Software
• -We service industry
Nice to have
• Please see the Pixlore photo of the boots. We were hoping that the desiger would be able ti modify the image with an overlay of 0's and 1's in a kind of "matrix" fashion to indicate that we are merging traditional labour work with software.
Should not have
• No medical symbols. Note that WE ARE NOT HEALTH CARE.

```html
<!DOCTYPE html>
<html lang="en">
<head>
<meta charset="utf-8">
<title>Veritrak Analytics – Safety Brochure</title>
<link href="https://fonts.googleapis.com/css2?family=Philosopher:wght@400;700&display=swap" rel="stylesheet">
<style>
  :root {
    --backdrop: #f4e3e3;
    --paper: #ffffff;
    --green: #9cc43a;
    --green-deep: #6fa52a;
    --green-title: #5aa83a;
    --green-soft: #d3e6a2;
    --ink: #2c2c2c;
    --ink-soft: #4a4a4a;
    --chart-teal: #3bbbd9;
    --chart-green: #8cc63f;
    --chart-purple: #9b4fb0;
    --chart-orange: #f07f22;
    --chart-red: #e04848;
    --chart-yellow: #f2d01e;
    --grid: #e3e3e3;
  }
  * { box-sizing: border-box; margin: 0; padding: 0; }
  html, body { width: 1200px; height: 1000px; overflow: hidden; }
  body {
    background: var(--backdrop);
    font-family: "Philosopher", "Trebuchet MS", sans-serif;
    color: var(--ink);
    position: relative;
  }
  .brochure {
    position: absolute;
    left: 252px; top: 50px;
    width: 696px; height: 900px;
    background: var(--paper);
    overflow: hidden;
  }
  .brand {
    position: absolute; top: 46px; left: 0; width: 100%;
    display: flex; justify-content: center; align-items: center; gap: 12px;
  }
  .brand-dot { width: 38px; height: 38px; border-radius: 50%; background: var(--green); }
  .brand-name { font-size: 30px; font-weight: 700; color: var(--ink-soft); letter-spacing: 1px; }

  .hero-band { position: absolute; top: 130px; left: 0; width: 100%; height: 230px; }
  .hero-band svg { position: absolute; inset: 0; }
  .hero-copy { position: absolute; top: 20px; left: 44px; right: 40px; color: var(--ink); }
  .hero-title { font-size: 28px; font-weight: 400; margin-bottom: 12px; }
  .hero-list { list-style: none; font-size: 17px; line-height: 1.45; }
  .hero-list li::before { content: "✓ "; }

  .features {
    position: absolute; top: 390px; left: 30px; right: 30px;
    display: flex; justify-content: space-between;
  }
  .feature { width: 200px; text-align: center; }
  .feature svg { display: block; margin: 0 auto 10px; }
  .feature-title { color: var(--green-title); font-size: 21px; font-weight: 400; margin-bottom: 6px; }
  .feature p { font-size: 14px; line-height: 1.55; color: var(--ink-soft); }
  .feature .feature-result { font-weight: 700; color: var(--ink); }

  .closing { position: absolute; top: 640px; left: 0; width: 100%; height: 180px; display: flex; }
  .closing-message {
    width: 270px; background: var(--green);
    display: flex; align-items: center; justify-content: center; text-align: center;
    font-size: 24px; line-height: 1.25; color: var(--ink); padding: 0 20px;
  }
  .closing-photo {
    flex: 1;
    background: radial-gradient(ellipse at 50% 65%, #8a7a4a 0%, #a9a46a 28%, var(--green-soft) 62%, #dcecb4 100%);
  }

  .contact {
    position: absolute; top: 836px; left: 0; width: 100%; text-align: center;
    font-size: 15px; line-height: 1.5; color: var(--ink);
  }
</style>
</head>
<body>
  <main class="brochure">
    <header class="brand">
      <span class="brand-dot"></span>
      <span class="brand-name">Veritrak Analytics</span>
    </header>

    <section class="hero-band">
      <svg width="696" height="230" viewBox="0 0 696 230" aria-hidden="true">
        <path d="M0 0 H696 V200 Q420 236 0 214 Z" fill="var(--green)"/>
      </svg>
      <div class="hero-copy">
        <h1 class="hero-title">Leverage the power of BIG DATA!</h1>
        <ul class="hero-list">
          <li>LEAD the next wave of injury reduction</li>
          <li>ENGAGE with members through collaboration and benchmarking</li>
          <li>PROMOTE standardization</li>
          <li>ANALYZE Accurate, Timely and Complete Leading Indicators</li>
          <li>TRAIN industry more proactively</li>
        </ul>
      </div>
    </section>

    <section class="features">
      <article class="feature">
        <svg width="200" height="140" viewBox="0 0 200 140" aria-label="Stacked bar chart of training hours">
          <rect width="200" height="140" fill="#fbfaf6"/>
          <text x="100" y="14" font-size="8" text-anchor="middle" fill="#555">Training Hours</text>
          <g stroke="var(--grid)"><line x1="22" y1="40" x2="196" y2="40"/><line x1="22" y1="70" x2="196" y2="70"/><line x1="22" y1="100" x2="196" y2="100"/><line x1="22" y1="125" x2="196" y2="125"/></g>
          <g>
            <rect x="28" y="118" width="20" height="7" fill="var(--chart-orange)"/><rect x="28" y="80" width="20" height="38" fill="var(--chart-green)"/><rect x="28" y="62" width="20" height="18" fill="var(--chart-teal)"/>
            <rect x="56" y="118" width="20" height="7" fill="var(--chart-orange)"/><rect x="56" y="70" width="20" height="48" fill="var(--chart-green)"/><rect x="56" y="50" width="20" height="20" fill="var(--chart-teal)"/><rect x="56" y="42" width="20" height="8" fill="var(--chart-purple)"/>
            <rect x="84" y="118" width="20" height="7" fill="var(--chart-orange)"/><rect x="84" y="92" width="20" height="26" fill="var(--chart-green)"/><rect x="84" y="80" width="20" height="12" fill="var(--chart-teal)"/>
            <rect x="112" y="118" width="20" height="7" fill="var(--chart-orange)"/><rect x="112" y="66" width="20" height="52" fill="var(--chart-green)"/><rect x="112" y="44" width="20" height="22" fill="var(--chart-teal)"/><rect x="112" y="36" width="20" height="8" fill="var(--chart-purple)"/>
            <rect x="140" y="118" width="20" height="7" fill="var(--chart-orange)"/><rect x="140" y="78" width="20" height="40" fill="var(--chart-green)"/><rect x="140" y="60" width="20" height="18" fill="var(--chart-purple)"/><rect x="140" y="48" width="20" height="12" fill="var(--chart-teal)"/>
            <rect x="168" y="118" width="20" height="7" fill="var(--chart-orange)"/><rect x="168" y="76" width="20" height="42" fill="var(--chart-purple)"/><rect x="168" y="56" width="20" height="20" fill="var(--chart-teal)"/>
          </g>
        </svg>
        <h2 class="feature-title">Training</h2>
        <p>Analyze needs of Industry<br>Deliver Proactive Training<br><span class="feature-result">Improve Safety</span></p>
      </article>

      <article class="feature">
        <svg width="140" height="140" viewBox="0 0 140 140" aria-label="Pie chart of incidents by type">
          <rect width="140" height="140" fill="#fff"/>
          <text x="70" y="12" font-size="8" text-anchor="middle" fill="#555">Incidents by Type</text>
          <g transform="translate(70 78)">
            <path d="M0 0 L0 -46 A46 46 0 0 1 46 2 Z" fill="var(--chart-teal)"/>
            <path d="M0 0 L46 2 A46 46 0 0 1 20 41 Z" fill="var(--chart-yellow)"/>
            <path d="M0 0 L20 41 A46 46 0 0 1 6 46 Z" fill="var(--chart-green)"/>
            <path d="M0 0 L6 46 A46 46 0 1 1 0 -46 Z" fill="var(--chart-red)"/>
          </g>
        </svg>
        <h2 class="feature-title">Benchmarking</h2>
        <p>Engage with Members<br>Promote Collaborative<br>Advancement of Safety<br><span class="feature-result">Improve Safety</span></p>
      </article>

      <article class="feature">
        <svg width="200" height="140" viewBox="0 0 200 140" aria-label="Grouped bar chart of industry trends">
          <rect width="200" height="140" fill="#fbfaf6"/>
          <text x="100" y="14" font-size="8" text-anchor="middle" fill="#555">Overview</text>
          <g stroke="var(--grid)"><line x1="18" y1="40" x2="196" y2="40"/><line x1="18" y1="70" x2="196" y2="70"/><line x1="18" y1="100" x2="196" y2="100"/><line x1="18" y1="110" x2="196" y2="110"/></g>
          <g>
            <rect x="22" y="60" width="5" height="50" fill="var(--chart-red)"/><rect x="27" y="80" width="5" height="30" fill="var(--chart-green)"/><rect x="32" y="92" width="5" height="18" fill="var(--chart-purple)"/>
            <rect x="42" y="30" width="5" height="80" fill="var(--chart-red)"/><rect x="47" y="70" width="5" height="40" fill="var(--chart-green)"/><rect x="52" y="86" width="5" height="24" fill="var(--chart-yellow)"/>
            <rect x="62" y="88" width="5" height="22" fill="var(--chart-red)"/><rect x="67" y="98" width="5" height="12" fill="var(--chart-purple)"/>
            <rect x="78" y="52" width="5" height="58" fill="var(--chart-red)"/><rect x="83" y="76" width="5" height="34" fill="var(--chart-green)"/><rect x="88" y="94" width="5" height="16" fill="var(--chart-teal)"/>
            <rect x="98" y="74" width="5" height="36" fill="var(--chart-red)"/><rect x="103" y="90" width="5" height="20" fill="var(--chart-yellow)"/><rect x="108" y="96" width="5" height="14" fill="var(--chart-purple)"/>
            <rect x="118" y="64" width="5" height="46" fill="var(--chart-red)"/><rect x="123" y="84" width="5" height="26" fill="var(--chart-green)"/>
            <rect x="136" y="80" width="5" height="30" fill="var(--chart-red)"/><rect x="141" y="86" width="5" height="24" fill="var(--chart-purple)"/><rect x="146" y="96" width="5" height="14" fill="var(--chart-teal)"/>
            <rect x="156" y="70" width="5" height="40" fill="var(--chart-red)"/><rect x="161" y="82" width="5" height="28" fill="var(--chart-green)"/>
            <rect x="174" y="78" width="5" height="32" fill="var(--chart-purple)"/><rect x="179" y="88" width="5" height="22" fill="var(--chart-red)"/><rect x="184" y="96" width="5" height="14" fill="var(--chart-yellow)"/>
          </g>
          <g>
            <rect x="30" y="124" width="10" height="5" fill="var(--chart-teal)"/><rect x="66" y="124" width="10" height="5" fill="var(--chart-yellow)"/><rect x="102" y="124" width="10" height="5" fill="var(--chart-green)"/><rect x="138" y="124" width="10" height="5" fill="var(--chart-red)"/>
          </g>
        </svg>
        <h2 class="feature-title">Trend Analysis</h2>
        <p>Monitor Industry Trends<br>Implement Corrective Initiatives<br><span class="feature-result">Improve Safety</span></p>
      </article>
    </section>

    <section class="closing">
      <div class="closing-message">THE NEXT BIG STEP<br>IN INJURY REDUCTION!<br>For your entire industry</div>
      <div class="closing-photo" role="img" aria-label="Photo of worn leather work boots standing on soil, tinted green"></div>
    </section>

    <footer class="contact">
      1-888-555-0142<br>www.veritrakdata.com
    </footer>
  </main>
</body>
</html>
```